Redesign of existing Web Design Project

I wish to redsesign the web pages on www.qbrl.com.au

Background of Harlowe Bexley

Harlowe Bexley Construction Services was established in 2004 as a boutique construction company offering construction advice and management services. We assist people in the construction minefield – step by step.

We offer services in: -

• Construction Management
• Project Management
• Building

The essence of our business is ensuring every project we undertake achieves the client’s objectives. Our experience has shown the secrets to a profitable project are -

• Planning
• Attention to detail
• Value add

We take the trouble to understand the client’s needs in person. Our hands-on approach ensures those involved deliver to the required quality standards at the scheduled times.

Our area of works include: -

• Residential single and multistorey developments
• Education facilities
• Suburban commercial building and refurbishment
• Health
• Defence
• Industrial

Objective of Acquisition

We are planning to expand our business activities. We are aiming to increase our turnover and use website as an increased passive selling tool.

Possible company type

This is an ideal opportunity for person who can capture readers attention.

Target Market(s)

see www.qbrl.com.au

Industry/Entity Type

Construction

Requirements
Must have
• Capture peoples attention on readers zones

```html
<!DOCTYPE html>
<html lang="en">
<head>
<meta charset="utf-8">
<title>Harlowe Bexley Construction Services</title>
<link href="https://fonts.googleapis.com/css2?family=Roboto+Condensed:wght@400;700&family=Arimo:ital,wght@0,400;0,700;1,400&display=swap" rel="stylesheet">
<style>
:root{
  --page:#dcdcdc;
  --dark:#23272a;
  --dark-2:#2f3437;
  --white:#ffffff;
  --ink:#1e2226;
  --nav-ink:#3a3d40;
  --accent:#6b7fc4;
  --accent-soft:#a9b5de;
  --muted:#444;
  --dots:#bdbdbd;
}
*{margin:0;padding:0;box-sizing:border-box}
html,body{width:1200px;height:1102px;overflow:hidden}
body{background:var(--page);font-family:"Arimo",Arial,sans-serif;color:var(--ink);position:relative}
.site-header{position:absolute;left:0;top:0;width:1200px;height:99px;background:linear-gradient(#26292c,#202326 85%,#0d0f10)}
.brand{position:absolute;left:92px;top:32px;display:flex;align-items:center;gap:12px;font-family:"Roboto Condensed",sans-serif;font-weight:400;font-size:30px;color:#d9def0;letter-spacing:.2px}
.brand-mark{width:40px;height:40px;background:#8fa0d8;display:block}
.page{position:absolute;left:88px;top:99px;width:1000px;height:935px;background:var(--white);border-radius:0 0 10px 10px;overflow:hidden}
.main-nav{height:63px;display:flex;justify-content:space-between;padding:0 12px 0 13px;border-bottom:1px solid #e6e6e6}
.main-nav a{font-family:"Roboto Condensed",sans-serif;font-weight:700;font-size:17px;color:var(--nav-ink);text-decoration:none;line-height:68px;position:relative}
.main-nav a.current::after{content:"";position:absolute;left:-13px;right:-22px;bottom:0;height:4px;background:var(--accent)}
.hero{position:absolute;left:0;top:64px;width:1000px;height:369px;background:linear-gradient(180deg,#c9c6f0 0%,#9f97cf 35%,#6f5f8a 60%,#3a3438 80%,#2a2624 100%)}
.hero-caption{position:absolute;left:0;bottom:0;width:1000px;height:102px;background:rgba(25,25,30,.55)}
.hero-caption p{position:absolute;left:82px;top:22px;width:600px;font-family:"Roboto Condensed",sans-serif;font-weight:700;font-size:18px;line-height:30px;color:#d2d2d6}
.hero-arrow{position:absolute;top:38px}
.hero-arrow.prev{left:14px}.hero-arrow.next{right:14px}
.hero-shadow{position:absolute;left:150px;top:433px;width:700px;height:40px;background:radial-gradient(ellipse at top,rgba(0,0,0,.12),rgba(0,0,0,0) 70%)}
.content{position:absolute;left:33px;top:466px;width:620px}
.section-title{font-family:"Roboto Condensed",sans-serif;font-weight:700;font-size:21px;color:var(--ink);display:inline-block;padding-bottom:1px;position:relative}
.title-bar{height:5px;display:flex}
.title-bar span:first-child{background:var(--accent-soft)}
.title-bar span:last-child{background:var(--accent)}
.content p{font-size:13.3px;line-height:30px;color:#111}
.lead{margin-top:13px}
.philosophy{margin-top:12px;font-weight:700;color:#222!important}
.quote{font-style:italic;color:var(--muted)!important}
.divider{border-top:1px dotted var(--dots);margin:14px 0 0;width:620px}
.testimonials{margin-top:34px}
.gallery{position:absolute;left:696px;top:474px;width:268px;height:168px;border-radius:10px;border:2px solid #e4e4e4;background:linear-gradient(160deg,#4c5470 0%,#6a6a8a 40%,#8a6c6a 62%,#2a2c36 100%);overflow:hidden}
.gallery h3{position:absolute;right:10px;top:62px;text-align:right;font-family:"Roboto Condensed",sans-serif;font-weight:700;font-size:21px;line-height:30px;color:#e6e6ea}
.gallery .more{position:absolute;left:0;bottom:0;width:100%;height:36px;background:rgba(20,20,25,.55);font-size:13.5px;color:#e0e0e0;padding:8px 14px}
.gallery-fold{position:absolute;left:908px;top:594px}
.brochure{position:absolute;left:696px;top:683px;width:268px;height:75px;border-radius:8px;background:linear-gradient(#f6f6f6,#d6d6d6)}
.brochure h3{position:absolute;left:9px;top:18px;font-family:"Roboto Condensed",sans-serif;font-weight:700;font-size:19px;color:#2a2c30}
.brochure small{position:absolute;left:10px;top:43px;font-family:"Roboto Condensed",sans-serif;font-size:13px;color:#444}
.brochure-folder{position:absolute;left:858px;top:658px;width:104px;height:86px;border-radius:4px;background:linear-gradient(#f2f0e8 0 28%,#8fa1ad 28%,#5e6f7a)}
.brochure-folder span{position:absolute;left:6px;bottom:6px;font-family:"Roboto Condensed",sans-serif;font-size:13px;color:#eef2f4}
.site-footer{position:absolute;left:0;bottom:0;width:1000px;height:43px;background:var(--dark);border-radius:0 0 10px 10px}
.site-footer p{font-size:11.5px;color:#e4e4e4;padding:15px 33px}
</style>
</head>
<body>
<header class="site-header">
  <div class="brand"><span class="brand-mark"></span>HARLOWE BEXLEY Construction Services</div>
</header>
<div class="page">
  <nav class="main-nav">
    <a class="current" href="#">About us</a><a href="#">Building</a><a href="#">Construction Management</a><a href="#">Project Management</a><a href="#">Links</a><a href="#">Free Downloads</a><a href="#">Careers</a><a href="#">Contact</a>
  </nav>
  <section class="hero" role="img" aria-label="Tower cranes over a waterfront construction site at dusk">
    <div class="hero-caption">
      <svg class="hero-arrow prev" width="30" height="34" viewBox="0 0 30 34"><path d="M14 2 2 17l12 15M28 2 16 17l12 15" fill="none" stroke="#b8b8bc" stroke-width="5"/></svg>
      <p>Lorem ipsum dolor sit amet, consectetuer adipiscing elit, sed diam nonummy nibh euismod tincidunt ut laoreet dolore magna aliquam erat volutpat.</p>
      <svg class="hero-arrow next" width="30" height="34" viewBox="0 0 30 34"><path d="M2 2l12 15L2 32M16 2l12 15-12 15" fill="none" stroke="#b8b8bc" stroke-width="5"/></svg>
    </div>
  </section>
  <div class="hero-shadow"></div>
  <main class="content">
    <h2 class="section-title">Welcome to Harlowe Bexley</h2>
    <div class="title-bar" style="width:271px"><span style="width:92px"></span><span style="flex:1"></span></div>
    <p class="lead">We are a Sydney based Construction Company who can help with all your construction needs. The Harlowe Bexley process helps define your budget, establishes Return on Investment and reduces potential risk.</p>
    <p class="philosophy">Our philosophy is simple:</p>
    <p class="quote">"Deliver the project you want on time, to budget."</p>
    <div class="divider"></div>
    <h2 class="section-title testimonials">Testimonials</h2>
    <div class="title-bar" style="width:130px"><span style="width:42px"></span><span style="flex:1"></span></div>
    <p class="lead">Harlowe Bexley is a construction company with significant skills in Project and Construction Management. We will help you undertake a successful construction.</p>
    <p class="quote">“The success of our Newcastle project built our confidence in the ability of Harlowe Bexley.”</p>
    <p>- Dale Prentice Director Corvane Constructions</p>
  </main>
  <a class="gallery" href="#" role="img" aria-label="Cranes on a building site at sunset">
    <h3>Project Gallery<br>Pictures</h3>
    <div class="more">Click here to see more
      <svg width="22" height="16" viewBox="0 0 22 16" style="vertical-align:middle;margin-left:14px"><path d="M2 1l6 7-6 7M11 1l6 7-6 7" fill="none" stroke="#b0b0b8" stroke-width="3"/></svg>
    </div>
  </a>
  <svg class="gallery-fold" width="62" height="58" viewBox="0 0 62 58"><path d="M62 0V58H0Z" fill="#fff"/><path d="M62 0 0 58" stroke="#d8d8d8"/></svg>
  <a class="brochure" href="#">
    <h3>Corporate Brochure</h3>
    <small>Click here to download</small>
  </a>
  <div class="brochure-folder" role="img" aria-label="Folder holding the brochure"><span>Download</span></div>
  <footer class="site-footer"><p>Copyright © 2012 Harlowe Bexley, All Rights Reserved</p></footer>
</div>
</body>
</html>
```